Webdesign für Management Coaching
Zielgruppe
Ich bin Coach/biete Coaching-Leistungen an.
Zielgruppe: Fokus auf Führungskräfte/Entscheider/Management mit technischem Hintergrund (Forschung & Entwicklung, Engineering, Technik, Maschinenbau, Naturwissenschaften)
Coaching-Schwerpunkte: Sinn-Coaching, Begleitung bei Umbrüchen und Veränderungen (privat & beruflich), Sparring & Reflexion
Aufgabenstellung
Gewünscht wurde ein helles Design, das die Logo-Farben aufnimmt. Ausrichtung am Logo & den verwendeten Farben, Schriften
Bilder: Ich werde noch Fotos beim Fotografen machen, die eingebunden werden sollen (Profil, etc.). Bitte Anhaltspunkte nennen, worauf ich die Fotografin hinweisen soll/welche Motive ins Konzept passen.

```html
<!DOCTYPE html>
<html lang="de">
<head>
<meta charset="utf-8">
<title>Lichtweg Coaching – Management Coaching</title>
<link rel="stylesheet" href="https://fonts.googleapis.com/css2?family=Gelasio:ital,wght@0,400;0,500;1,400;1,500;1,600&display=swap">
<style>
:root{
  --ink:#5a626c;
  --ink-soft:#7a828c;
  --accent:#7c9fba;
  --accent-dark:#6a8ea9;
  --tint:#f5f6f9;
  --card:#ffffff;
  --line:#dde2e8;
  --white:#ffffff;
}
*{box-sizing:border-box;margin:0;padding:0}
html,body{width:1200px;height:2189px;overflow:hidden;background:var(--white)}
body{font-family:"Gelasio",Georgia,serif;font-style:italic;color:var(--ink)}
.page{width:1200px;height:2189px;position:relative;overflow:hidden}
.wrap{padding:0 124px}
.btn{display:inline-flex;align-items:center;gap:8px;background:var(--accent);color:var(--white);font-size:14px;font-weight:600;padding:5px 12px;border-radius:2px;text-decoration:none}
.btn svg{width:16px;height:12px}
.eyebrow{color:var(--accent);font-size:16px}
.h2{font-size:36px;font-weight:500;color:var(--ink);margin-top:6px}

/* header */
.site-header{position:absolute;top:0;left:0;right:0;height:130px;display:flex;align-items:center;justify-content:space-between;padding:0 124px;z-index:2}
.main-nav{display:flex;gap:30px;font-size:14px}
.brand{position:absolute;left:50%;top:22px;transform:translateX(-50%);display:flex;flex-direction:column;align-items:center;gap:8px}
.brand-dot{width:56px;height:56px;border-radius:50%;border:1px solid var(--line)}
.brand-name{font-size:13px;color:var(--accent);letter-spacing:1px}
.header-actions{display:flex;align-items:center;gap:12px}
.social{width:16px;height:16px;border-radius:50%;background:var(--accent)}

/* hero */
.hero{position:absolute;top:0;left:0;right:0;height:522px}
.hero-photo{position:absolute;left:470px;top:110px;right:0;bottom:0;
  background:radial-gradient(ellipse at 62% 45%,#cdc7c4 0%,#e3ded9 30%,#f3eeea 55%,rgba(255,255,255,0) 80%),
  linear-gradient(90deg,#fff 0%,#f2efec 30%,#ebe6e2 70%,#f4f2f0 100%)}
.hero-copy{position:absolute;left:124px;top:190px;width:420px}
.hero-title{font-size:44px;font-weight:400;line-height:1.18}
.hero-sub{color:var(--accent);font-size:18px;line-height:1.55;margin:24px 0 24px}

/* about */
.about{position:absolute;top:522px;left:0;right:0;height:543px;display:flex;padding:60px 124px 0;gap:108px}
.about-photo{width:382px;height:424px;border-radius:3px;background:linear-gradient(160deg,#8e949a 0%,#b6b2ab 45%,#7d8fa3 100%)}
.about-copy{width:462px;padding-top:46px}
.about-copy .h2{margin-bottom:22px}
.about-copy p{font-size:15px;line-height:1.75;color:var(--ink-soft);margin-bottom:24px}

/* offer */
.offer{position:absolute;top:1065px;left:0;right:0;height:535px;background:var(--tint);padding:14px 124px 0}
.center{text-align:center}
.offer-grid{display:flex;gap:28px;margin-top:34px}
.offer-list{width:462px;display:flex;flex-direction:column;gap:14px}
.offer-item{background:var(--card);height:113px;padding:18px 18px;position:relative}
.offer-item.active{box-shadow:0 3px 10px rgba(90,98,108,.12)}
.offer-item.active::after{content:"";position:absolute;right:-10px;top:44px;border:10px solid transparent;border-left-color:var(--card);border-right:0}
.offer-item svg{width:24px;height:20px;display:block}
.offer-item h3{font-size:18px;font-weight:500;color:var(--accent);margin:6px 0 4px}
.offer-item p{font-size:14px;color:var(--ink-soft)}
.offer-detail{width:462px;background:var(--card);padding:16px 16px 14px;display:flex;flex-direction:column}
.offer-detail p{font-size:15px;line-height:1.6;text-align:center;color:var(--ink-soft)}
.offer-visual{height:222px;margin:10px 0 12px;background:linear-gradient(135deg,#c7d1db 0%,#aebccb 55%,#d6dde4 100%)}
.offer-detail .btn{align-self:flex-end}

/* clients */
.clients{position:absolute;top:1600px;left:0;right:0;height:466px;padding:58px 124px 0}
.client-grid{display:flex;gap:28px;margin-top:28px}
.client{flex:1;background:var(--tint);padding:16px 18px 18px}
.client-head{display:flex;gap:12px;align-items:flex-start}
.client-head svg{width:26px;height:26px;flex:none}
.client-name{color:var(--accent);font-size:17px;font-weight:500;line-height:1}
.client-role{font-size:12px;color:var(--ink-soft)}
.quote{width:40px;height:26px;margin:12px 0 8px}
.client p{font-size:14px;line-height:1.95;color:var(--ink-soft)}

/* footer */
.site-footer{position:absolute;top:2066px;left:0;right:0;bottom:0;background:var(--tint);padding:18px 124px 0}
.footer-top{display:flex;justify-content:space-between;align-items:flex-start;height:72px}
.footer-brand{display:flex;flex-direction:column;align-items:center;gap:4px;margin-left:10px}
.footer-brand .brand-dot{width:34px;height:34px}
.footer-brand .brand-name{font-size:10px}
.footer-right{display:flex;flex-direction:column;align-items:flex-end;gap:12px}
.footer-nav{display:flex;gap:24px;font-size:13px}
.footer-social{display:flex;gap:12px}
.footer-bottom{border-top:1px solid var(--line);display:flex;justify-content:space-between;padding-top:8px;font-size:12px}
.legal{display:flex;gap:24px}
</style>
</head>
<body>
<div class="page">

  <section class="hero">
    <div class="hero-photo" role="img" aria-label="Frau sitzt auf einem Felsen und blickt in eine sonnige Berglandschaft"></div>
    <div class="hero-copy">
      <h1 class="hero-title">Lorem ipsum dolor sit amen</h1>
      <p class="hero-sub">Lorem ipsum dolor sit amen,<br>consetetur sadipscing elitr</p>
      <a class="btn" href="#">Termin buchen
        <svg viewBox="0 0 16 14" fill="none" stroke="currentColor" stroke-width="1.2"><rect x="3" y="2" width="10" height="11"/><line x1="3" y1="5" x2="13" y2="5"/><line x1="6" y1="0.5" x2="6" y2="3"/><line x1="10" y1="0.5" x2="10" y2="3"/></svg>
      </a>
    </div>
  </section>

  <header class="site-header">
    <nav class="main-nav"><span>Home</span><span>Leistungen</span><span>Über mich</span><span>Blog</span></nav>
    <div class="brand"><span class="brand-dot"></span><span class="brand-name">Lichtweg Coaching</span></div>
    <div class="header-actions">
      <span class="social" aria-label="Soziales Netzwerk"></span>
      <span class="social" aria-label="Berufliches Netzwerk"></span>
      <a class="btn" href="#">Kontakt
        <svg viewBox="0 0 16 12" fill="none" stroke="currentColor" stroke-width="1.2"><path d="M2 1h12v7H7l-3 3V8H2z"/></svg>
      </a>
    </div>
  </header>

  <section class="about">
    <div class="about-photo" role="img" aria-label="Porträt des Coaches mit grauem Haar und Brille, lächelnd"></div>
    <div class="about-copy">
      <div class="eyebrow">Ein bisschen zu mir</div>
      <h2 class="h2">Hi, ich bin Matthias</h2>
      <p>Lorem ipsum dolor sit amet, consetetur sadipscing elitr, sed diam nonumy eirmod tempor invidunt ut labore et dolore magna aliquyam erat, sed diam voluptua. At vero eos et accusam et justo duo dolores et ea rebum. Stet clita kasd gubergren, no sea takimata sanctus est Lorem ipsum dolor sit amet. Lorem ipsum dolor sit amet, consetetur sadipscing elitr, sed diam nonumy eirmod tempor invidunt</p>
      <a class="btn" href="#">Mehr über mich
        <svg viewBox="0 0 18 10" fill="none" stroke="currentColor" stroke-width="1.2"><path d="M1 5h15M12 1l4 4-4 4"/></svg>
      </a>
    </div>
  </section>

  <section class="offer">
    <div class="center">
      <div class="eyebrow">Lorem ipsum</div>
      <h2 class="h2">Mein Angebot für Dich</h2>
    </div>
    <div class="offer-grid">
      <div class="offer-list">
        <div class="offer-item active">
          <svg viewBox="0 0 24 20" fill="none" stroke="#7c9fba" stroke-width="1.6"><circle cx="12" cy="10" r="8"/><circle cx="12" cy="10" r="3"/></svg>
          <h3>Sinn-Coaching</h3>
          <p>Lorem ipsum dolor sit amet, consetetur</p>
        </div>
        <div class="offer-item">
          <svg viewBox="0 0 24 20" fill="none" stroke="#7c9fba" stroke-width="1.6"><path d="M2 10h20M2 10c6 0 8-7 20-7M2 10c6 0 8 7 20 7"/></svg>
          <h3>Begleitung bei Veränderung</h3>
          <p>Lorem ipsum dolor sit amet, consetetur</p>
        </div>
        <div class="offer-item">
          <svg viewBox="0 0 24 20" fill="none" stroke="#7c9fba" stroke-width="1.6"><path d="M3 3h18v11H9l-4 4v-4H3z"/></svg>
          <h3>Sparring &amp; Reflexion</h3>
          <p>Lorem ipsum dolor sit amet, consetetur</p>
        </div>
      </div>
      <div class="offer-detail">
        <p>Lorem ipsum dolor sit amet, consetetur sadipscing elitr, sed diam nonumy eirmod tempor invidunt ut labore et dolore magna aliquyam erat, sed diam</p>
        <div class="offer-visual" role="img" aria-label="Offene Hand unter einer Wortwolke zu Coaching, Potential, Ziel und Wissen"></div>
        <a class="btn" href="#">Mehr erfahren
          <svg viewBox="0 0 18 10" fill="none" stroke="currentColor" stroke-width="1.2"><path d="M1 5h15M12 1l4 4-4 4"/></svg>
        </a>
      </div>
    </div>
  </section>

  <section class="clients">
    <div class="eyebrow">Lorem ipsum</div>
    <h2 class="h2">More happy Clients...</h2>
    <div class="client-grid">
      <article class="client">
        <div class="client-head">
          <svg viewBox="0 0 26 26" fill="#7c9fba"><circle cx="13" cy="8" r="6"/><path d="M2 25c0-7 5-10 11-10s11 3 11 10z"/></svg>
          <div><div class="client-name">Max Muster</div><div class="client-role">Sample Manager</div></div>
        </div>
        <svg class="quote" viewBox="0 0 40 26" fill="#a9bfd1"><path d="M2 14c0-7 4-12 10-13v4c-3 1-5 3-5 6h5v14H2zM22 14c0-7 4-12 10-13v4c-3 1-5 3-5 6h5v14H22z"/></svg>
        <p>Lorem ipsum dolor sit amet, consetetur sadipscing elitr, sed diam nonumy eirmod tempor invidunt ut labore et dolore magna aliquyam erat, sed diam voluptua. At vero eos et accusam et justo duo dolores et ea</p>
      </article>
      <article class="client">
        <div class="client-head">
          <svg viewBox="0 0 26 26" fill="#7c9fba"><circle cx="13" cy="8" r="6"/><path d="M2 25c0-7 5-10 11-10s11 3 11 10z"/></svg>
          <div><div class="client-name">Max Muster</div><div class="client-role">Sample Manager</div></div>
        </div>
        <svg class="quote" viewBox="0 0 40 26" fill="#a9bfd1"><path d="M2 14c0-7 4-12 10-13v4c-3 1-5 3-5 6h5v14H2zM22 14c0-7 4-12 10-13v4c-3 1-5 3-5 6h5v14H22z"/></svg>
        <p>Lorem ipsum dolor sit amet, consetetur sadipscing elitr, sed diam nonumy eirmod tempor invidunt ut labore et dolore magna aliquyam erat, sed diam voluptua. At vero eos et accusam et justo duo dolores et ea</p>
      </article>
      <article class="client">
        <div class="client-head">
          <svg viewBox="0 0 26 26" fill="#7c9fba"><circle cx="13" cy="8" r="6"/><path d="M2 25c0-7 5-10 11-10s11 3 11 10z"/></svg>
          <div><div class="client-name">Max Muster</div><div class="client-role">Sample Manager</div></div>
        </div>
        <svg class="quote" viewBox="0 0 40 26" fill="#a9bfd1"><path d="M2 14c0-7 4-12 10-13v4c-3 1-5 3-5 6h5v14H2zM22 14c0-7 4-12 10-13v4c-3 1-5 3-5 6h5v14H22z"/></svg>
        <p>Lorem ipsum dolor sit amet, consetetur sadipscing elitr, sed diam nonumy eirmod tempor invidunt ut labore et dolore magna aliquyam erat, sed diam voluptua. At vero eos et accusam et justo duo dolores et ea</p>
      </article>
    </div>
  </section>

  <footer class="site-footer">
    <div class="footer-top">
      <div class="footer-brand"><span class="brand-dot"></span><span class="brand-name">Lichtweg Coaching</span></div>
      <div class="footer-right">
        <nav class="footer-nav"><span>Home</span><span>Leistungen</span><span>Über mich</span><span>Blog</span></nav>
        <div class="footer-social"><span class="social" aria-label="Soziales Netzwerk"></span><span class="social" aria-label="Berufliches Netzwerk"></span></div>
      </div>
    </div>
    <div class="footer-bottom">
      <span>© 2024 atelier-muster.de</span>
      <span class="legal"><span>Impressum</span><span>Datenschutz</span></span>
    </div>
  </footer>

</div>
</body>
</html>
```